Business card design for strategy and management consulting company. Would like to have a clean and professional business card, based on the attached logo. The company is a strategy and management consulting company focusing on sustainable business modlels based on economic, social and environmental market opportunities. Preferably the logo should be included on both sides of the design.

Industry/Entity Type

Business

Contact Information for Business Card

Håvard Lilleby, CEO/Management consultant
havard.lilleby@quarvenpartners.example
Mob: +47 948 26 317
Office: Vikfjell gate 14, pb 312 sentrum, N-0172 Oslo Norway

Requirements
Must have
• Include attached logo
Nice to have
• Would like to have the logo on both sides
Should not have
• Many colours.

```html
<!DOCTYPE html>
<html lang="en">
<head>
<meta charset="utf-8">
<title>Quarven business card</title>
<link rel="stylesheet" href="https://fonts.googleapis.com/css2?family=Work+Sans:wght@300;400;500;600&display=swap">
<style>
  :root {
    --backdrop: #2b2b2c;
    --card: #1c1c1d;
    --card-edge: #151516;
    --ink-white: #f4f4f4;
    --ink-grey: #cfcfcf;
    --ink-muted: #454547;
    --accent: #f2e200;
  }
  * { margin: 0; padding: 0; box-sizing: border-box; }
  html, body {
    width: 1200px; height: 900px; overflow: hidden;
    background: var(--backdrop);
    font-family: "Work Sans", Arial, sans-serif;
  }
  .canvas {
    position: relative; width: 1200px; height: 900px;
  }
  .card {
    position: absolute; left: 290px; width: 620px; height: 354px;
    background: var(--card);
    border: 1px solid var(--card-edge);
    box-shadow: 0 10px 28px rgba(0,0,0,.45);
  }
  .card--back { top: 62px; }
  .card--front { top: 478px; }

  .wordmark {
    font-family: "Work Sans", Arial, sans-serif;
    font-weight: 600;
    letter-spacing: -1px;
    display: flex; align-items: center; gap: 12px;
  }
  .wordmark__dot {
    width: 12px; height: 12px; border-radius: 50%;
  }
  .card--back .wordmark {
    position: absolute; left: 0; right: 0; top: 118px;
    justify-content: center;
    font-size: 92px; line-height: 1; color: var(--ink-muted);
  }
  .card--back .wordmark__dot { background: var(--ink-muted); width: 16px; height: 16px; }

  .card--front .wordmark {
    position: absolute; right: 42px; top: 34px;
    font-size: 62px; line-height: 1; color: var(--ink-white);
  }
  .card--front .wordmark__dot { background: var(--accent); }

  .person { position: absolute; left: 48px; top: 150px; }
  .person__name {
    font-size: 27px; font-weight: 500; color: var(--accent); line-height: 1.1;
  }
  .person__role {
    font-size: 15px; font-weight: 300; color: var(--ink-grey); margin-top: 4px;
  }
  .rule {
    position: absolute; left: 40px; right: 40px; top: 218px;
    height: 2px; background: var(--accent);
  }
  .contact {
    position: absolute; left: 48px; top: 236px; list-style: none;
    font-size: 15px; font-weight: 300; color: var(--ink-grey);
  }
  .contact__item { display: flex; align-items: center; gap: 12px; height: 24px; }
  .contact__icon { width: 12px; height: 12px; flex: none; }
  .address {
    position: absolute; right: 42px; bottom: 30px; text-align: right;
    font-size: 16px; font-weight: 300; color: var(--ink-grey); line-height: 1.35;
    font-style: normal;
  }
</style>
</head>
<body>
<main class="canvas">
  <section class="card card--back" aria-label="Card back">
    <div class="wordmark"><span>Quarven</span><span class="wordmark__dot"></span></div>
  </section>

  <section class="card card--front" aria-label="Card front">
    <div class="wordmark"><span>Quarven</span><span class="wordmark__dot"></span></div>

    <div class="person">
      <p class="person__name">Håvard Lilleby</p>
      <p class="person__role">CEO/Management consultant</p>
    </div>

    <div class="rule"></div>

    <ul class="contact">
      <li class="contact__item">
        <svg class="contact__icon" viewBox="0 0 12 12" aria-hidden="true">
          <rect x="3" y="0.8" width="6" height="10.4" rx="1" fill="none" stroke="#f2e200" stroke-width="1.2"/>
          <line x1="5" y1="9.3" x2="7" y2="9.3" stroke="#f2e200" stroke-width="1"/>
        </svg>
        <span>+47 948 26 317</span>
      </li>
      <li class="contact__item">
        <svg class="contact__icon" viewBox="0 0 12 12" aria-hidden="true">
          <rect x="0.8" y="2.3" width="10.4" height="7.4" fill="none" stroke="#f2e200" stroke-width="1.2"/>
          <polyline points="0.8,2.5 6,6.6 11.2,2.5" fill="none" stroke="#f2e200" stroke-width="1.1"/>
        </svg>
        <span>havard.lilleby@quarvenpartners.example</span>
      </li>
    </ul>

    <address class="address">
      Vikfjell gate 14,<br>
      pb 312 sentrum, Oslo Norway
    </address>
  </section>
</main>
</body>
</html>
```